I already have a logo created by Quillory Makers that I'm very happy with. I need to spruce up my business card now. Its a double sided card with not much info on it, I like to keep it simple.
Front of card: name, phone # email address, web address. Tag Line "Outsourced Technology Solutions", under that it says Business Voice Services & Electronic Protection.
Rear of Card: Content written inside a "cloud" saying "Cloud Solutions" "Cloud Integrity"

Target Market(s)

Business to Business

Industry/Entity Type

Business

Contact Information for Business Card

We are in the technology field. Providing Telephone systems (hardware), SIP Trunks (dial tone/local/long distance/telephone #'s), LAN (Local Area Network)infrastructure cabling, Data Center solutions and Security Applications (Camera systems, Access Control systems,

Requirements
Must have
• Must have brevity
Should not have
• Clutter and/or too much information

```html
<!DOCTYPE html>
<html lang="en">
<head>
<meta charset="utf-8">
<title>Summit Relay Networks – Business Card</title>
<link href="https://fonts.googleapis.com/css2?family=Open+Sans:wght@600;700&family=Raleway:wght@400;500;600&display=swap" rel="stylesheet">
<style>
  :root {
    --navy: #1f4590;
    --grey: #7b7f86;
    --paper: #ffffff;
    --backdrop: #e9ecef;
    --shadow: rgba(20, 30, 50, 0.18);
  }
  * { box-sizing: border-box; margin: 0; padding: 0; }
  html, body {
    width: 1200px;
    height: 1200px;
    overflow: hidden;
    background: var(--backdrop);
  }
  .canvas {
    width: 1200px;
    height: 1200px;
    display: flex;
    flex-direction: column;
    align-items: center;
    justify-content: center;
    gap: 70px;
  }
  .card {
    width: 840px;
    height: 480px;
    background: var(--paper);
    box-shadow: 0 10px 30px var(--shadow);
    position: relative;
    overflow: hidden;
  }

  /* Back side: cloud message with brand name */
  .card-back {
    display: flex;
    flex-direction: column;
    align-items: center;
    justify-content: center;
    gap: 26px;
  }
  .cloud {
    width: 400px;
    height: 220px;
    display: block;
  }
  .cloud-outline {
    fill: none;
    stroke: var(--navy);
    stroke-width: 6;
    stroke-linejoin: round;
  }
  .cloud-text {
    font-family: "Raleway", sans-serif;
    font-weight: 600;
    font-size: 28px;
    fill: var(--navy);
  }
  .card-back .brand {
    display: flex;
    align-items: center;
    gap: 16px;
  }
  .card-back .brand-mark {
    width: 30px;
    height: 30px;
    background: var(--navy);
  }
  .card-back .brand-name {
    font-family: "Raleway", sans-serif;
    font-weight: 600;
    font-size: 32px;
    color: var(--navy);
  }

  /* Front side */
  .card-front .identity {
    position: absolute;
    left: 100px;
    top: 40px;
    display: flex;
    align-items: center;
    gap: 22px;
  }
  .card-front .brand-mark {
    width: 40px;
    height: 40px;
    background: var(--navy);
    flex: none;
  }
  .card-front .brand-name {
    font-family: "Raleway", sans-serif;
    font-weight: 600;
    font-size: 40px;
    line-height: 1.05;
    color: var(--navy);
  }
  .card-front .tagline {
    position: absolute;
    left: 120px;
    top: 150px;
    font-family: "Raleway", sans-serif;
    font-weight: 400;
    font-size: 27px;
    color: var(--grey);
    border-bottom: 2px solid var(--grey);
    padding-bottom: 2px;
  }
  .card-front .services {
    position: absolute;
    left: 120px;
    top: 201px;
    font-family: "Raleway", sans-serif;
    font-weight: 500;
    font-size: 20px;
    color: var(--grey);
  }
  .card-front .band {
    position: absolute;
    left: 0;
    right: 0;
    top: 248px;
    height: 30px;
    background: var(--navy);
  }
  .contact {
    position: absolute;
    top: 318px;
    font-family: "Open Sans", sans-serif;
    font-weight: 700;
    font-size: 24px;
    color: var(--navy);
    line-height: 43px;
    list-style: none;
  }
  .contact-personal { left: 42px; }
  .contact-company { right: 42px; top: 361px; text-align: right; }
</style>
</head>
<body>
  <main class="canvas">
    <section class="card card-back" aria-label="Card back">
      <svg class="cloud" viewBox="0 0 400 220" aria-label="Cloud Solutions, Cloud Integrity">
        <path class="cloud-outline" d="M90 200 H320 A60 60 0 0 0 330 82 A80 80 0 0 0 180 50 A65 65 0 0 0 80 100 A52 52 0 0 0 90 200 Z"/>
        <text class="cloud-text" x="205" y="130" text-anchor="middle">Cloud Solutions</text>
        <text class="cloud-text" x="205" y="170" text-anchor="middle">Cloud Integrity</text>
      </svg>
      <div class="brand">
        <span class="brand-mark"></span>
        <span class="brand-name">Summit Relay Networks, LLC</span>
      </div>
    </section>

    <section class="card card-front" aria-label="Card front">
      <div class="identity">
        <span class="brand-mark"></span>
        <h1 class="brand-name">Summit Relay<br>Networks, LLC</h1>
      </div>
      <p class="tagline">Outsourced Technology Solutions</p>
      <p class="services">Business Voice Services &amp; Electronic Protection</p>
      <div class="band"></div>
      <ul class="contact contact-personal">
        <li>Name</li>
        <li>Phone</li>
        <li>Email</li>
      </ul>
      <ul class="contact contact-company">
        <li>Address</li>
        <li>Web Address</li>
      </ul>
    </section>
  </main>
</body>
</html>
```